Inspiration Poster

Inspirational Poster that has a Kamran Dulo like abstract look (http://www.vexalo.com/images/search?q=kamran+dulo&FORM=HDRSC2) with the text:

"we walk not in order to arrive at the promise land but because walking itself is a revolution"
-Peter Ambrick

```html
<!DOCTYPE html>
<html lang="en">
<head>
<meta charset="utf-8">
<title>Walking Itself Is a Revolution</title>
<link rel="stylesheet" href="https://fonts.googleapis.com/css2?family=Alfa+Slab+One&family=Squada+One&display=swap">
<style>
  :root {
    --page: #ffffff;
    --ink: #ffffff;
    --denim-deep: #141f38;
    --denim-mid: #2c4266;
    --denim-light: #7f9dbd;
    --haze: #c7d6e6;
    --streak: #c98a5a;
    --blank-fill: #d9dde2;
    --revolution: #f4a46f;
    --revolution-light: #fbe3b0;
  }
  html, body {
    margin: 0;
    padding: 0;
    width: 1200px;
    height: 1000px;
    overflow: hidden;
    background: var(--page);
  }
  .poster {
    display: block;
    width: 1200px;
    height: 1000px;
  }
  .quote-line {
    font-family: "Squada One", "Arial Narrow", sans-serif;
    fill: var(--ink);
    text-transform: uppercase;
  }
  .blank-frame { fill: var(--ink); }
  .blank-fill { fill: var(--blank-fill); }
  .headline-word {
    font-family: "Alfa Slab One", Georgia, serif;
    fill: url(#revolutionTone);
  }
  .attribution {
    font-family: "Squada One", "Arial Narrow", sans-serif;
    fill: var(--ink);
  }
</style>
</head>
<body>
<svg class="poster" viewBox="0 0 1200 1000" xmlns="http://www.w3.org/2000/svg">
  <defs>
    <linearGradient id="denimTone" x1="0" y1="1" x2="1" y2="0">
      <stop offset="0" stop-color="var(--denim-deep)"/>
      <stop offset="0.45" stop-color="var(--denim-mid)"/>
      <stop offset="0.85" stop-color="var(--denim-light)"/>
      <stop offset="1" stop-color="var(--haze)"/>
    </linearGradient>
    <radialGradient id="warmGlow" cx="0.45" cy="0.28" r="0.45">
      <stop offset="0" stop-color="var(--streak)" stop-opacity="0.35"/>
      <stop offset="1" stop-color="var(--streak)" stop-opacity="0"/>
    </radialGradient>
    <linearGradient id="revolutionTone" x1="0" y1="0" x2="1" y2="0">
      <stop offset="0" stop-color="var(--revolution)"/>
      <stop offset="0.5" stop-color="var(--revolution)"/>
      <stop offset="1" stop-color="var(--revolution-light)"/>
    </linearGradient>
  </defs>

  <g class="backdrop" role="img" aria-label="Grainy denim-textured photograph of an open road with warm light streaks">
    <rect x="0" y="105" width="1200" height="800" fill="url(#denimTone)"/>
    <rect x="0" y="105" width="1200" height="800" fill="url(#warmGlow)"/>
  </g>

  <g class="quote">
    <text class="quote-line" x="305" y="412" font-size="88" textLength="363" lengthAdjust="spacingAndGlyphs">We walk not</text>
    <rect class="blank-frame" x="686" y="342" width="212" height="70"/>
    <rect class="blank-fill" x="694" y="349" width="196" height="56"/>

    <text class="quote-line" x="305" y="467" font-size="54" textLength="593" lengthAdjust="spacingAndGlyphs">In order to arrive at the promise land</text>

    <text class="quote-line" x="305" y="602" font-size="170" textLength="170" lengthAdjust="spacingAndGlyphs">But</text>
    <text class="quote-line" x="488" y="540" font-size="82" textLength="410" lengthAdjust="spacingAndGlyphs">Because walking</text>

    <rect class="blank-frame" x="488" y="552" width="212" height="50"/>
    <rect class="blank-fill" x="495" y="558" width="198" height="38"/>
    <text class="quote-line" x="706" y="602" font-size="60" textLength="192" lengthAdjust="spacingAndGlyphs">Itself is a</text>
  </g>

  <text class="headline-word" x="30" y="815" font-size="190" textLength="1140" lengthAdjust="spacingAndGlyphs">REVOLUTION</text>

  <text class="attribution" x="1168" y="878" font-size="48" text-anchor="end">-Peter Ambrick</text>
</svg>
</body>
</html>
```